Website design for Harbor Bolts. ( Lock company)

Harbor Bolts is a New York Based Company that manufactures a variety of high quality Locks which sell worldwide.

Our website: We need a 'face' on the Internet , a website that tells you who we are and what we do - 'An Identity'.

it is not an eCommerce website . the website is to show customers and potential distributers who we are and what we manufacture ( so they come away with a great impression of our company and our products) see www.quarrelwheel.com

First glance impression: We are Professional; are locks are strong,and reliable. and we are ready to compete with other major Lock companies

Content: for starters the site will contain general information and background about our company (our story), were to buy our products, contact information, and display images of our Locks (and of course all the classic links including to all the legal and technical information). as time goes on we will add more features to the website i.e. Products, Videos blogs etc.

although at first there will not be that much content on the website - it should not look empty (it should be simple and clear but not empty) it should look and feel like a full fledged professional website (not a template)

Inspiration: here are a few sites which have the feel we are looking for:

General tone - quarrelwheel.com bramhold.com (black is good - But not a must )

Simplicity, clarity - coldvane.com panwright.com

the widescreen Image look - http://www.pagecritter.com/demo/58261.html

we are considering perhaps having wide HQ images of Lion(s) in the background (but without the felling that it is a zoo or safari website) - it is not a must, its just an idea .

perhaps (if you find it looks good ) use a bit of that metal or chrome look to give it it a strong smooth feel (however it should not look like a dark prison)

We do not currently have a Logo ( if you feel you can design one that fits the above company description - we would love to see if it can work for us) We can talk about additional funds for the logo during this project.

Our working slogan is : Harbor Bolts - "Keeper of your Ground"

for your convenience we have attached a few images of the type of locks we sell

We are looking to collaborate with you throughout the project. We have ideas and visions we want implemented and we will help you along the way. So we can create the perfect website.

Thank you.

```html
<!DOCTYPE html>
<html lang="en">
<head>
<meta charset="utf-8">
<title>Harbor Bolts – Keeper of your Ground</title>
<link href="https://fonts.googleapis.com/css2?family=Oswald:wght@400;500;700&family=Open+Sans:wght@400;600;700&display=swap" rel="stylesheet">
<style>
:root{
  --red:#c8161d;
  --red-dark:#9e0f15;
  --ink:#111111;
  --panel:#1b1b1b;
  --panel-2:#232323;
  --line:#333333;
  --text:#bdbdbd;
  --muted:#8a8a8a;
  --white:#ffffff;
  --steel-1:#9aa0a6;
  --steel-2:#3b3f44;
}
*{margin:0;padding:0;box-sizing:border-box}
html,body{width:686px;height:1200px;overflow:hidden;background:var(--ink)}
body{font-family:"Open Sans",Arial,sans-serif;color:var(--text);position:relative}
.page{position:relative;width:686px;height:1200px;background:var(--panel)}

/* navigation */
.nav{position:absolute;top:0;left:98px;width:490px;height:34px;display:flex;z-index:3}
.nav-item{flex:1;padding:6px 4px 0 8px;color:var(--white);font:600 6.5px/1.2 "Open Sans",sans-serif;text-transform:uppercase}
.nav-item small{display:block;color:var(--muted);font-weight:400;font-size:5px;text-transform:none;margin-top:1px}
.nav-item.is-active{background:var(--red)}
.nav-item.is-active small{color:#f3c7c9}

/* hero */
.hero{position:absolute;top:0;left:0;width:686px;height:270px;overflow:hidden}
.hero-photo{position:absolute;inset:0;background:radial-gradient(ellipse at 75% 45%,#6a5538 0%,#3a2e22 30%,#1c1712 60%,#0e0c0a 100%)}
.nav-band{position:absolute;top:0;left:0;width:686px;height:34px;background:rgba(0,0,0,.55)}
.hero-brand{position:absolute;top:98px;left:0;width:686px;text-align:center}
.brand-mark{width:40px;height:40px;border-radius:50%;border:2px solid var(--white);margin:0 auto 10px}
.brand-name{font:700 34px/1 "Oswald",sans-serif;color:var(--white);letter-spacing:1px;text-transform:uppercase}
.brand-slogan{font:700 17px/1 "Oswald",sans-serif;color:var(--white);margin-top:8px;text-transform:uppercase;letter-spacing:.5px}
.hero-arrow{position:absolute;top:158px;width:12px;height:20px}
.hero-arrow.prev{left:100px}.hero-arrow.next{right:100px}

/* section headings */
.section-title{position:absolute;left:98px;font:500 11px/1 "Oswald",sans-serif;color:var(--red);text-transform:uppercase}
.section-lead{position:absolute;left:98px;width:490px;font-size:5.5px;line-height:1.55;color:var(--text)}

/* products */
.products{position:absolute;top:315px;left:98px;width:490px;display:flex;justify-content:space-between}
.product{width:66px;text-align:center}
.product-photo{width:66px;height:110px;border-radius:4px;background:linear-gradient(180deg,#b8bcc1 0%,#6c7177 55%,#2a2d31 100%)}
.product-photo.brass{background:linear-gradient(180deg,#d7b36a 0%,#9c7634 60%,#3a2b12 100%)}
.product-photo.black{background:linear-gradient(180deg,#5a5d61 0%,#2a2c2f 60%,#121314 100%)}
.product-name{font:600 5px/1 "Open Sans",sans-serif;color:var(--white);margin-top:8px;text-transform:uppercase}
.slider-arrow{position:absolute;top:368px;width:8px;height:14px}

/* feature banners */
.feature{position:absolute;top:528px;width:234px;height:124px;overflow:hidden;background:var(--panel-2)}
.feature-photo{position:absolute;inset:0;background:linear-gradient(110deg,#2a2a2a 0%,#4b4f54 45%,#9ea3a8 75%,#5b5f64 100%)}
.feature.electronic .feature-photo{background:linear-gradient(110deg,#1f1f1f 0%,#3f4246 50%,#c9a25a 82%,#6d5a32 100%)}
.feature-body{position:absolute;left:10px;top:14px;width:120px}
.feature-title{font:700 17px/1 "Oswald",sans-serif;color:var(--white);text-transform:uppercase}
.feature-copy{font-size:5px;line-height:1.5;color:#e0e0e0;margin-top:6px}
.btn{display:inline-block;background:var(--red);color:var(--white);font:700 5.5px/1 "Open Sans",sans-serif;text-transform:uppercase;padding:5px 9px}
.feature .btn{margin-top:8px}

/* welcome */
.welcome-band{position:absolute;top:744px;left:98px;width:490px;height:68px;background:linear-gradient(90deg,#3a3a3a,#8a8a8a 50%,#3a3a3a)}
.welcome-cols{position:absolute;top:824px;left:98px;width:490px;display:flex;gap:20px}
.welcome-cols .col{flex:1;font-size:5px;line-height:1.6;color:var(--text)}
.welcome-cols p+p{margin-top:8px}
.read-more{position:absolute;top:956px;left:311px;padding:5px 12px}

/* mailing list */
.mailing{position:absolute;top:1004px;left:0;width:686px;height:36px;background:#2a2a2a;border-top:1px solid var(--line);border-bottom:1px solid var(--line)}
.mailing-label{position:absolute;left:98px;top:13px;font:500 9px/1 "Oswald",sans-serif;color:var(--white);text-transform:uppercase}
.mailing-label span{color:var(--red)}
.mailing-input{position:absolute;left:198px;top:11px;width:130px;height:14px;background:#3a3a3a;font-size:5px;color:var(--muted);padding:4px 5px}
.mailing .btn{position:absolute;left:334px;top:11px;padding:4px 9px}
.follow{position:absolute;left:430px;top:13px;font:500 8px/1 "Oswald",sans-serif;color:var(--white);text-transform:uppercase}
.social{position:absolute;left:478px;top:9px;display:flex;gap:5px}
.social i{width:16px;height:16px;border-radius:50%;background:#5a5a5a;display:block}

/* footer */
.footer{position:absolute;top:1041px;left:0;width:686px;height:125px;background:#161616}
.footer-brand{position:absolute;left:98px;top:32px}
.footer-brand .name{font:700 20px/1 "Oswald",sans-serif;color:var(--white);text-transform:uppercase}
.footer-brand .slogan{font:700 8px/1 "Oswald",sans-serif;color:var(--white);margin-top:4px;text-transform:uppercase}
.footer-col{position:absolute;top:18px;font-size:5px;line-height:1.9;color:var(--text)}
.footer-col li{list-style:none}
.footer-col li::before{content:"› ";color:var(--red)}
.footer-col.contact li::before{content:""}
.copyright{position:absolute;top:1166px;left:0;width:686px;height:34px;background:var(--ink);text-align:center;font-size:5px;line-height:34px;color:var(--muted)}
.to-top{position:absolute;right:98px;top:1178px;width:10px;height:10px}
</style>
</head>
<body>
<div class="page">

  <header class="hero">
    <div class="hero-photo" role="img" aria-label="Wide dark photograph of a lion's head in low light"></div>
    <div class="nav-band"></div>
    <nav class="nav">
      <div class="nav-item is-active">Home<small>Welcome to our home</small></div>
      <div class="nav-item">About Us<small>Who we are</small></div>
      <div class="nav-item">Products<small>Our lock range</small></div>
      <div class="nav-item">Services<small>What we offer</small></div>
      <div class="nav-item">Testimonials<small>Client words</small></div>
      <div class="nav-item">Online Shop<small>Where to buy</small></div>
      <div class="nav-item">Contact Us<small>Get in touch</small></div>
    </nav>
    <svg class="hero-arrow prev" viewBox="0 0 12 20"><path d="M10 2 2 10l8 8" fill="none" stroke="#fff" stroke-width="2"/></svg>
    <svg class="hero-arrow next" viewBox="0 0 12 20"><path d="M2 2l8 8-8 8" fill="none" stroke="#fff" stroke-width="2"/></svg>
    <div class="hero-brand">
      <div class="brand-mark"></div>
      <div class="brand-name">Harbor Bolts</div>
      <div class="brand-slogan">Keeper of your Ground</div>
    </div>
  </header>

  <h2 class="section-title" style="top:282px">Our Products</h2>
  <p class="section-lead" style="top:297px">Strong, reliable locks engineered in New York and trusted by homes, shops and distributors in every corner of the world.</p>

  <svg class="slider-arrow" style="left:84px" viewBox="0 0 8 14"><path d="M7 1 1 7l6 6" fill="none" stroke="#888" stroke-width="1.5"/></svg>
  <svg class="slider-arrow" style="left:594px" viewBox="0 0 8 14"><path d="M1 1l6 6-6 6" fill="none" stroke="#888" stroke-width="1.5"/></svg>
  <div class="products">
    <div class="product"><div class="product-photo" role="img" aria-label="Steel padlock with blue body"></div><div class="product-name">Lorem Ipsum</div></div>
    <div class="product"><div class="product-photo black" role="img" aria-label="Black padlock"></div><div class="product-name">Lorem Ipsum</div></div>
    <div class="product"><div class="product-photo" role="img" aria-label="Silver padlock with long shackle"></div><div class="product-name">Lorem Ipsum</div></div>
    <div class="product"><div class="product-photo brass" role="img" aria-label="Brass door knob set"></div><div class="product-name">Lorem Ipsum</div></div>
    <div class="product"><div class="product-photo brass" role="img" aria-label="Brass lever handle set"></div><div class="product-name">Lorem Ipsum</div></div>
    <div class="product"><div class="product-photo" role="img" aria-label="Steel padlock with blue casing"></div><div class="product-name">Lorem Ipsum</div></div>
  </div>

  <section class="feature smart" style="left:98px">
    <div class="feature-photo" role="img" aria-label="Heavy chain wrapped around a steel padlock"></div>
    <div class="feature-body">
      <div class="feature-title">Smart<br>Security</div>
      <p class="feature-copy">Hardened steel and precise mechanisms that keep what matters safe, day and night.</p>
      <span class="btn">Click Here</span>
    </div>
  </section>
  <section class="feature electronic" style="left:354px">
    <div class="feature-photo" role="img" aria-label="Key turning in a brass door lock"></div>
    <div class="feature-body">
      <div class="feature-title">Electronic<br>Locks</div>
      <p class="feature-copy">Keyless entry with smart codes, built for modern homes and busy offices.</p>
      <span class="btn">Click Here</span>
    </div>
  </section>

  <h2 class="section-title" style="top:680px">Welcome to Harbor Bolts</h2>
  <p class="section-lead" style="top:698px">Harbor Bolts is a New York based company that manufactures a wide range of high quality locks sold worldwide. Every product we make is designed, tested and finished to give customers and distributors lasting confidence in their security.</p>

  <div class="welcome-band" role="img" aria-label="Wide grey photograph of a padlock on a metal door"></div>

  <div class="welcome-cols">
    <div class="col">
      <p>Our story began in a small workshop with one simple goal: to build locks that never let people down. Today our team designs padlocks, door hardware and electronic locks that meet strict standards for strength and reliability, shipped to partners across many countries.</p>
      <p>We work closely with distributors to bring the right products to every market, backed by clear support and honest service.</p>
    </div>
    <div class="col">
      <p>Each lock is made from carefully chosen materials and checked at every stage of production. From the shackle to the smallest pin, we focus on the details that keep doors, gates and cases secure for years to come.</p>
      <p>Find out where to buy our products, read about our range, or contact our team to start a partnership today.</p>
    </div>
  </div>
  <span class="btn read-more">Read More</span>

  <section class="mailing">
    <div class="mailing-label">Join <span>Our</span> Mailing List</div>
    <div class="mailing-input">Enter your email here</div>
    <span class="btn">Submit Now</span>
    <div class="follow">Follow Us</div>
    <div class="social"><i></i><i></i><i></i><i></i></div>
  </section>

  <footer class="footer">
    <div class="footer-brand">
      <div class="name">Harbor Bolts</div>
      <div class="slogan">Keeper of your Ground</div>
    </div>
    <ul class="footer-col" style="left:262px">
      <li>Home</li><li>About Us</li><li>Products</li><li>Services</li><li>Testimonials</li><li>Online Shop</li><li>Contact Us</li>
    </ul>
    <ul class="footer-col" style="left:340px">
      <li>Our Story</li><li>Where to Buy</li><li>Pricing</li><li>Careers</li><li>News</li>
    </ul>
    <ul class="footer-col" style="left:418px">
      <li>Terms &amp; Payments</li><li>Privacy Policy</li><li>Disclaimer</li>
    </ul>
    <ul class="footer-col contact" style="left:506px">
      <li>Address</li><li>100 Harbor Street</li><li>New York, NY 10001</li><li>Tel: 555 0100</li><li>info@harborbolts.com</li>
    </ul>
  </footer>
  <div class="copyright">Copyright © 2024 Harbor Bolts. All Rights Reserved.</div>
  <svg class="to-top" viewBox="0 0 10 10"><path d="M1 7l4-4 4 4" fill="none" stroke="#888" stroke-width="1.5"/></svg>

</div>
</body>
</html>
```